Harborline Crest Insurance Services

we are a high end insurance agency we specialize on Auto | Home | Business | Life looking for something professional and luxuries at the same time. if you guys need anything else please let me know.

Auto | Home | Business | Life must be under logo on the back with black background.

i want the back part to be black with our gold logo on it.

Target Market(s)

Auto | Home | Business | Life

Industry/Entity Type

Insurance Broker

Contact Information for Business Card

My logo is gold so a black in the back would be nice.

Font styles to use
Serif

Colors
000000

Requirements
Must have
• Big logo on the back with black background.

```html
<!DOCTYPE html>
<html lang="en">
<head>
<meta charset="utf-8">
<title>Harborline Crest Insurance Services – Business Card</title>
<link rel="stylesheet" href="https://fonts.googleapis.com/css2?family=Cinzel:wght@400;600;700&family=Lato:wght@400;700&display=swap">
<style>
  :root {
    --backdrop: #3a3a3a;
    --card-dark: #2a2a2a;
    --card-dark-deep: #222222;
    --card-light: #ffffff;
    --card-light-shade: #ececec;
    --gold: #e2b00f;
    --gold-deep: #c99a08;
    --grey-text: #b9b9b9;
    --grey-line: #8a8a8a;
    --white-text: #f2f2f2;
  }
  * { box-sizing: border-box; margin: 0; padding: 0; }
  html, body { width: 1200px; height: 873px; overflow: hidden; }
  body {
    background: var(--backdrop);
    display: flex;
    align-items: center;
    justify-content: center;
    gap: 40px;
    font-family: "Lato", Arial, sans-serif;
  }
  .card {
    position: relative;
    width: 540px;
    height: 309px;
    overflow: hidden;
    box-shadow: 0 14px 30px rgba(0,0,0,.45);
  }

  /* Back of card */
  .card-back {
    background: linear-gradient(160deg, var(--card-dark) 0%, var(--card-dark-deep) 100%);
  }
  .back-brand {
    position: absolute;
    left: 0; right: 0; top: 80px;
    display: flex;
    flex-direction: column;
    align-items: center;
    gap: 14px;
  }
  .back-brand .brand-dot {
    width: 38px; height: 38px;
    border-radius: 50%;
    background: var(--gold);
  }
  .back-brand .brand-name {
    font-family: "Cinzel", Georgia, serif;
    font-weight: 600;
    font-size: 30px;
    color: var(--gold);
    text-align: center;
    line-height: 1.2;
  }
  .back-rule {
    position: absolute;
    left: 30px; right: 30px; bottom: 46px;
    height: 1px;
    background: var(--grey-line);
  }
  .back-services {
    position: absolute;
    left: 0; right: 0; bottom: 20px;
    text-align: center;
    font-size: 12px;
    letter-spacing: 3px;
    color: var(--gold);
    font-weight: 700;
  }
  .back-services .sep { color: var(--grey-text); margin: 0 6px; }

  /* Front of card */
  .card-front { background: var(--card-dark); }
  .front-top {
    position: absolute;
    left: 0; right: 0; top: 0;
    height: 150px;
    background: linear-gradient(180deg, var(--card-light) 0%, var(--card-light-shade) 100%);
  }
  .front-brand {
    position: absolute;
    left: 120px; top: 50px;
    display: flex;
    align-items: center;
    gap: 14px;
  }
  .front-brand .brand-dot {
    width: 30px; height: 30px;
    border-radius: 50%;
    background: var(--gold);
  }
  .front-brand .brand-name {
    font-family: "Cinzel", Georgia, serif;
    font-weight: 600;
    font-size: 19px;
    line-height: 1.2;
    color: var(--gold);
  }
  .front-stripes {
    position: absolute;
    left: 0; right: 0; top: 150px;
    height: 24px;
    background: var(--card-light-shade);
  }
  .front-stripes .stripe {
    position: absolute; left: 0; right: 0;
    height: 3px;
    background: var(--card-dark);
  }
  .front-stripes .stripe:nth-child(1) { top: 6px; }
  .front-stripes .stripe:nth-child(2) { top: 14px; }

  .holder {
    position: absolute;
    left: 30px; top: 212px;
    width: 210px;
  }
  .holder-name {
    font-family: "Cinzel", Georgia, serif;
    font-weight: 600;
    font-size: 20px;
    color: var(--gold);
    letter-spacing: .5px;
  }
  .holder-role {
    display: flex;
    align-items: center;
    gap: 8px;
    font-family: "Cinzel", Georgia, serif;
    font-size: 14px;
    color: var(--grey-text);
    letter-spacing: 1px;
    margin-top: 2px;
  }
  .holder-role::before,
  .holder-role::after {
    content: ""; flex: 1; height: 1px; background: var(--grey-text);
  }
  .holder-acn {
    font-size: 10px;
    color: var(--grey-text);
    margin-top: 12px;
    padding-left: 50px;
  }
  .divider {
    position: absolute;
    left: 262px; top: 196px;
    width: 2px; height: 96px;
    background: linear-gradient(180deg, transparent, var(--gold), transparent);
  }
  .contacts {
    position: absolute;
    left: 282px; top: 200px;
    list-style: none;
  }
  .contacts li {
    display: flex;
    align-items: center;
    gap: 12px;
    height: 21px;
    font-size: 13px;
    color: var(--white-text);
  }
  .contacts svg { width: 14px; height: 14px; fill: var(--gold-deep); flex: none; }
  .contacts .web { color: var(--gold); font-weight: 700; font-size: 14px; }
</style>
</head>
<body>

  <section class="card card-back" aria-label="Card back">
    <div class="back-brand">
      <span class="brand-dot"></span>
      <span class="brand-name">Harborline Crest<br>Insurance Services</span>
    </div>
    <div class="back-rule"></div>
    <p class="back-services">AUTO<span class="sep">•</span>HOME<span class="sep">•</span>BUSINESS<span class="sep">•</span>LIFE</p>
  </section>

  <section class="card card-front" aria-label="Card front">
    <div class="front-top">
      <div class="front-brand">
        <span class="brand-dot"></span>
        <span class="brand-name">Harborline Crest<br>Insurance Services</span>
      </div>
    </div>
    <div class="front-stripes"><span class="stripe"></span><span class="stripe"></span></div>

    <div class="holder">
      <p class="holder-name">DANIEL PORTER</p>
      <p class="holder-role">DIRECTOR</p>
      <p class="holder-acn">ACN 418 206 957</p>
    </div>

    <div class="divider"></div>

    <ul class="contacts">
      <li>
        <svg viewBox="0 0 24 24" aria-hidden="true"><path d="M6.6 10.8a15.1 15.1 0 0 0 6.6 6.6l2.2-2.2a1 1 0 0 1 1-.25 11.4 11.4 0 0 0 3.6.57 1 1 0 0 1 1 1V20a1 1 0 0 1-1 1A17 17 0 0 1 3 4a1 1 0 0 1 1-1h3.5a1 1 0 0 1 1 1c0 1.25.2 2.45.57 3.57a1 1 0 0 1-.25 1z"/></svg>
        0412 587 203
      </li>
      <li>
        <svg viewBox="0 0 24 24" aria-hidden="true"><path d="M2 5h20v14H2z M4 7v.5l8 5 8-5V7l-8 5z" fill-rule="evenodd"/></svg>
        daniel@hcis.com
      </li>
      <li>
        <svg viewBox="0 0 24 24" aria-hidden="true"><path d="M12 2a7 7 0 0 0-7 7c0 5.2 7 13 7 13s7-7.8 7-13a7 7 0 0 0-7-7zm0 9.5A2.5 2.5 0 1 1 12 6.5a2.5 2.5 0 0 1 0 5z"/></svg>
        Po Box 512 , Kelso ACT 2611
      </li>
      <li>
        <svg viewBox="0 0 24 24" aria-hidden="true"><path d="M10.6 13.4a1 1 0 0 0 1.4 0l4-4a1 1 0 1 0-1.4-1.4l-4 4a1 1 0 0 0 0 1.4zM8.5 11 6.4 13.1a3 3 0 0 0 4.2 4.3l2.1-2.1 1.4 1.4-2.1 2.1a5 5 0 0 1-7.1-7.1l2.1-2.1zM15.5 13l2.1-2.1a3 3 0 1 0-4.2-4.2L11.3 8.7 9.9 7.3 12 5.2a5 5 0 0 1 7.1 7.1L17 14.4z"/></svg>
        <span class="web">www.hcis.com</span>
      </li>
    </ul>
  </section>

</body>
</html>
```